Business Card Design for Pastor/Church Leadership - simple, elegant, "different"

Design a name card based on logo and color from our branding guide - see file "BWF Logo and Color".
The teal frame around the logo is not part of the logo and is a not necessary design element for the name card (as the attached PDF file may suggest).
The font suggested by branding is "Frutiger 55 Roman".
The file "not good.pdf", a sample of a name card that is NOT good.
- fonts too small to read
- the tagline on the logo "Still waters, bright path" not easy to read with logo used in this design
- "MAPLE GROVE CHAPEL" unnecessarily duplicated - possibly because logo too small
- not sure about the green frame, probably better to drop

Target Market(s)

broad, all people the pastor of an international church in Tokyo meets

Industry/Entity Type

Business

Contact Information for Business Card

Everett L. Pranzoni
Pastor
3-9-4 Kamiyacho, Shibuya-ku
Tokyo 150-0082 (Church)
2-18 Sarugakucho, Shibuya-ku
Tokyo 150-0046 (Home)
Tel: 03-5712-0368
E-mail: pastor@maplegrovechapel.org
URL: http://www.maplegrovechapel.org

Font styles to use
Sans Serif
Other font styles liked:
• Frutiger 55 Roman (want, not must)

Requirements
Must have
• must include logo
• must make use of the "bright turquoise color"
• Cyan = 59, Magenta = 0, Yellow=24, Black=0
• Red=3.1%, Green=91%, Blue=87.1%
• Key Info (name) must be easy to read (see notes on bad sample namecard attached)

```html
<!DOCTYPE html>
<html lang="en">
<head>
<meta charset="utf-8">
<title>Maple Grove Chapel – Pastor Business Card</title>
<link rel="stylesheet" href="https://fonts.googleapis.com/css2?family=Hind:wght@400;500&display=swap">
<style>
  :root {
    --page-bg: #d9d6d2;
    --card-bg: #3a3a3a;
    --card-bg-light: #414141;
    --turquoise: #5fc4c8;
    --white: #ffffff;
  }
  html, body {
    margin: 0;
    padding: 0;
    width: 1200px;
    height: 902px;
    overflow: hidden;
    background: var(--page-bg);
    font-family: "Hind", "Frutiger", sans-serif;
  }
  .business-card {
    position: absolute;
    left: 100px;
    top: 148px;
    width: 1000px;
    height: 606px;
    background: linear-gradient(135deg, var(--card-bg-light) 0%, var(--card-bg) 55%, var(--card-bg-light) 100%);
    box-shadow: 0 18px 40px rgba(0,0,0,0.35);
    color: var(--white);
  }
  .brand-mark {
    position: absolute;
    left: 150px;
    top: 110px;
    display: flex;
    align-items: center;
    gap: 16px;
    color: var(--turquoise);
    font-size: 84px;
    font-weight: 500;
    line-height: 1;
  }
  .brand-mark .mark-square {
    width: 30px;
    height: 30px;
    background: var(--turquoise);
  }
  .church-name {
    position: absolute;
    left: 92px;
    top: 262px;
    width: 330px;
    color: var(--turquoise);
    text-align: center;
  }
  .church-name .name {
    font-size: 30px;
    font-weight: 400;
    letter-spacing: 0.5px;
    padding-bottom: 4px;
    border-bottom: 2px solid var(--turquoise);
    white-space: nowrap;
  }
  .church-name .tagline {
    font-size: 29px;
    margin-top: 6px;
    letter-spacing: 0.8px;
    white-space: nowrap;
  }
  .church-address {
    position: absolute;
    left: 100px;
    top: 392px;
    display: flex;
    gap: 34px;
    color: var(--turquoise);
    font-size: 27px;
    line-height: 1.05;
  }
  .church-address .lines { padding-top: 6px; }
  .pastor-identity {
    position: absolute;
    left: 548px;
    top: 58px;
    text-align: center;
  }
  .pastor-identity .person-name {
    font-size: 42px;
    letter-spacing: 0.6px;
    white-space: nowrap;
  }
  .pastor-identity .role {
    font-size: 36px;
    color: var(--turquoise);
    line-height: 1;
    margin-top: -4px;
  }
  .contact-list {
    position: absolute;
    left: 580px;
    top: 245px;
    margin: 0;
    padding: 0;
    list-style: none;
    font-size: 25px;
    line-height: 1.05;
  }
  .contact-list li {
    display: flex;
    align-items: flex-start;
    gap: 18px;
    margin-bottom: 14px;
  }
  .contact-list .icon {
    width: 26px;
    flex: 0 0 26px;
    display: flex;
    justify-content: center;
  }
  .website {
    position: absolute;
    left: 0;
    right: 0;
    top: 540px;
    text-align: center;
    color: var(--turquoise);
    font-size: 26px;
    letter-spacing: 0.4px;
  }
</style>
</head>
<body>
  <section class="business-card">
    <div class="brand-mark">
      <span class="mark-square"></span>
      <span class="mark-name">BWF</span>
    </div>

    <div class="church-name">
      <div class="name">MAPLE GROVE CHAPEL</div>
      <div class="tagline">Still waters, bright path</div>
    </div>

    <div class="church-address">
      <svg width="20" height="28" viewBox="0 0 20 28" aria-hidden="true">
        <path d="M10 1C5 1 1.5 4.6 1.5 9.3 1.5 15.5 10 26 10 26s8.5-10.5 8.5-16.7C18.5 4.6 15 1 10 1z" fill="var(--turquoise)"/>
        <circle cx="10" cy="9.5" r="3.4" fill="var(--card-bg)"/>
      </svg>
      <div class="lines">
        3-9-4 Kamiyacho<br>
        Shibuya-ku<br>
        Tokyo 150-0082
      </div>
    </div>

    <div class="pastor-identity">
      <div class="person-name">Everett L. Pranzoni</div>
      <div class="role">Pastor</div>
    </div>

    <ul class="contact-list">
      <li>
        <span class="icon">
          <svg width="18" height="28" viewBox="0 0 18 28" aria-hidden="true">
            <rect x="1.5" y="1.5" width="15" height="25" rx="2.5" fill="none" stroke="var(--white)" stroke-width="2"/>
            <line x1="6" y1="22.5" x2="12" y2="22.5" stroke="var(--white)" stroke-width="2"/>
          </svg>
        </span>
        <span>03-5712-0368</span>
      </li>
      <li>
        <span class="icon">
          <svg width="26" height="18" viewBox="0 0 26 18" aria-hidden="true">
            <rect x="0" y="0" width="26" height="18" fill="var(--white)"/>
            <path d="M1 1l12 9 12-9" fill="none" stroke="var(--card-bg)" stroke-width="2"/>
          </svg>
        </span>
        <span>pastor@maplegrovechapel.org</span>
      </li>
      <li>
        <span class="icon">
          <svg width="18" height="26" viewBox="0 0 20 28" aria-hidden="true">
            <path d="M10 1C5 1 1.5 4.6 1.5 9.3 1.5 15.5 10 26 10 26s8.5-10.5 8.5-16.7C18.5 4.6 15 1 10 1z" fill="var(--white)"/>
            <circle cx="10" cy="9.5" r="3.4" fill="var(--card-bg)"/>
          </svg>
        </span>
        <span>2-18 Sarugakucho<br>Shibuya-ku<br>Tokyo 150-0046</span>
      </li>
    </ul>

    <div class="website">http://www.maplegrovechapel.org</div>
  </section>
</body>
</html>
```